Ronan Pike Building Business Card Design

Hi,

I need a business card for my Building company.
I am a Builder and build homes for clients.
I am looking for a sophisticated logo that can be used on business cards, envelopes and letter heads.
I am trying to take my business to the next level and need a professional business card.

Colours: Please use white, black, dark grey and bright blue.

Thank you,

Marnie and Ronan.

Target Market(s)

1. Home and Building Companies 2. Potential customers

Industry/Entity Type

Business

Contact Information for Business Card

Ronan Pike Building PTY LTD

Ronan Pike

Director

A.B.N. 37 902 518 617

BUILDERS LICENCE No. 573019k

Mobile: 0471 283 906

Email: ronanpikebuilding@maildrop-example.com.au

Requirements
Must have
• The following is compulsory to have in the designs:

Ronan Pike Building PTY LTD (business name)

Ronan Pike (contact name)

Director (position)

A.B.N. 37 902 518 617

Builders Licence No. 573019k

Mobile: 0471 283 906

Nice to have
• Logo for business
Should not have
• Should not be cluttered.

I am looking for a clean, sophisticated and professional business card design.

```html
<!DOCTYPE html>
<html lang="en">
<head>
<meta charset="utf-8">
<title>Ronan Pike Building – Business Card</title>
<link href="https://fonts.googleapis.com/css2?family=Orbitron:wght@800&family=Lato:wght@400&family=Questrial&display=swap" rel="stylesheet">
<style>
  :root {
    --page-bg: #ffffff;
    --card-front-light: #ffffff;
    --card-front-shade: #ededed;
    --card-border: #cfcfcf;
    --brand-blue: #29abe2;
    --brand-blue-deep: #1b86b8;
    --dark-grey: #a3a3a3;
    --text-grey: #5e5e5e;
    --ink: #111111;
    --white: #ffffff;
  }
  * { margin: 0; padding: 0; box-sizing: border-box; }
  html, body {
    width: 1200px;
    height: 900px;
    overflow: hidden;
    background: var(--page-bg);
  }
  .canvas {
    position: relative;
    width: 1200px;
    height: 900px;
  }
  .card {
    position: absolute;
    left: 267px;
    width: 666px;
    height: 411px;
    border: 1px solid var(--card-border);
    text-align: center;
  }

  /* Front */
  .card--front {
    top: 33px;
    background: radial-gradient(ellipse at 45% 40%, var(--card-front-light) 0%, var(--card-front-shade) 100%);
  }
  .brand-mark {
    position: absolute;
    left: 0;
    right: 0;
    top: 65px;
    height: 140px;
    display: flex;
    align-items: center;
    justify-content: center;
    gap: 18px;
  }
  .brand-mark__square {
    width: 44px;
    height: 44px;
    background: var(--dark-grey);
    border-radius: 3px;
  }
  .brand-mark__name {
    font-family: "Orbitron", sans-serif;
    font-weight: 800;
    font-size: 46px;
    letter-spacing: 3px;
    color: var(--brand-blue);
    white-space: nowrap;
  }
  .wordmark {
    position: absolute;
    left: 0;
    right: 0;
    top: 250px;
    font-family: "Orbitron", sans-serif;
    font-weight: 800;
    color: var(--brand-blue);
    font-size: 34px;
    letter-spacing: 2px;
    white-space: nowrap;
  }
  .wordmark__suffix {
    font-size: 16px;
    letter-spacing: 1px;
    margin-left: 8px;
  }
  .front-rule {
    position: absolute;
    left: 33px;
    width: 601px;
    top: 309px;
    height: 5px;
    background: var(--dark-grey);
  }
  .registration {
    position: absolute;
    left: 0;
    right: 0;
    top: 328px;
    font-family: "Lato", sans-serif;
    font-size: 13.5px;
    line-height: 20px;
    color: var(--text-grey);
  }

  /* Back */
  .card--back {
    top: 457px;
    background: var(--brand-blue);
  }
  .contact-name {
    position: absolute;
    left: 0;
    right: 0;
    top: 42px;
    padding-left: 8px;
    font-family: "Orbitron", sans-serif;
    font-weight: 800;
    font-size: 46px;
    letter-spacing: 8px;
    color: var(--white);
    white-space: nowrap;
  }
  .house-illustration {
    position: absolute;
    left: 243px;
    top: 127px;
    width: 180px;
    height: 116px;
    background: linear-gradient(160deg, #3a96bd 0%, #2c7fa6 50%, #5fb7dc 100%);
    border-radius: 4px;
  }
  .back-rule {
    position: absolute;
    left: 28px;
    width: 601px;
    top: 278px;
    height: 6px;
    background: var(--brand-blue-deep);
    box-shadow: 0 1px 0 rgba(255,255,255,0.25);
  }
  .role {
    position: absolute;
    left: 0;
    right: 0;
    top: 290px;
    font-family: "Questrial", sans-serif;
    font-size: 28px;
    color: var(--white);
  }
  .contact-details {
    position: absolute;
    left: 0;
    right: 0;
    top: 329px;
    font-family: "Questrial", sans-serif;
    font-size: 14px;
    line-height: 19px;
    color: var(--ink);
  }
</style>
</head>
<body>
  <main class="canvas">
    <section class="card card--front" aria-label="Business card front">
      <div class="brand-mark">
        <span class="brand-mark__square"></span>
        <span class="brand-mark__name">RONAN PIKE</span>
      </div>
      <h1 class="wordmark">RONAN PIKE BUILDING<span class="wordmark__suffix">PTY LTD</span></h1>
      <div class="front-rule"></div>
      <p class="registration">
        A.B.N. 37 902 518 617<br>
        BUILDERS LICENCE No. 573019k
      </p>
    </section>

    <section class="card card--back" aria-label="Business card back">
      <h2 class="contact-name">RONAN PIKE</h2>
      <div class="house-illustration" role="img" aria-label="Illustration of a two-storey house shown half as a blueprint sketch and half as a rendered model"></div>
      <div class="back-rule"></div>
      <p class="role">Director</p>
      <p class="contact-details">
        Mobile: 0471 283 906<br>
        Email: ronanpikebuilding@maildrop-example.com.au
      </p>
    </section>
  </main>
</body>
</html>
```